New business card design needed for Trucking/Staffing company!

I am looking for a business card design. The business name is Harbor Lane Freightworks, LLC. This company is a staffing company for commercial drivers/truck drivers. Most of our customers are trucking/supply companies. Our colors are blue/black/white/grey. The info I have on my current business cards is
-Spot for a name
-2 lines for an address
-3 lines for Office, cell, and fax
-email
-website(currently on backside of card with logo but can go anywhere)
Updates

Project Deadline Extended
Reason: Open to more designs

Target Market(s)

Trucking companies, building supply companies

Industry/Entity Type

Business

Contact Information for Business Card

Edgy but professional

Font styles to use
Other font styles liked:
• Open to suggestions

Colors
0555a3
000000
ffffff
9d9d9d

Requirements
Must have
• Must have the logo incorporated

```html
<!DOCTYPE html>
<html lang="en">
<head>
<meta charset="utf-8">
<title>Harbor Lane Freightworks, LLC – Business Card</title>
<link rel="stylesheet" href="https://fonts.googleapis.com/css2?family=Montserrat:wght@500;600;700&family=Open+Sans:wght@400;600&display=swap">
<style>
  :root {
    --page: #d9d4cc;
    --charcoal: #2b2b2b;
    --brand-blue: #363a8a;
    --brand-blue-light: #4a4fb0;
    --white: #ffffff;
    --silver-dark: #8a8a8a;
    --silver-light: #f2f2f2;
    --card-w: 830px;
    --card-h: 480px;
  }
  * { margin: 0; padding: 0; box-sizing: border-box; }
  html, body {
    width: 1130px; height: 1200px; overflow: hidden;
    background: var(--page);
  }
  .canvas { position: relative; width: 1130px; height: 1200px; }
  .card {
    position: absolute; left: 150px;
    width: var(--card-w); height: var(--card-h);
    background: var(--charcoal);
    overflow: hidden;
    box-shadow: 0 6px 16px rgba(0,0,0,0.25);
  }
  .card--front { top: 70px; }
  .card--back { top: 640px; }
  .card__bands { position: absolute; inset: 0; width: 100%; height: 100%; }

  .brand-name {
    position: absolute;
    font-family: "Montserrat", sans-serif;
    font-weight: 700;
    text-transform: uppercase;
    letter-spacing: 0.02em;
    white-space: nowrap;
  }
  .card--front .brand-name {
    left: 0; right: 0; top: 130px; text-align: center;
    font-size: 40px; color: var(--brand-blue-light);
  }
  .card--back .brand-name {
    left: 0; right: 0; top: 72px; text-align: center;
    font-size: 30px; color: var(--white);
  }
  .website {
    position: absolute; left: 0; right: 0; top: 375px; text-align: center;
    font-family: "Open Sans", sans-serif; font-weight: 600;
    font-size: 31px; color: var(--white);
  }

  .contact { position: absolute; left: 215px; top: 186px; color: var(--white); font-family: "Open Sans", sans-serif; }
  .contact__name { font-family: "Montserrat", sans-serif; font-weight: 600; font-size: 29px; line-height: 1.2; }
  .contact__position { font-size: 25px; line-height: 1.3; color: #e6e6e6; margin-bottom: 22px; }
  .contact__list { list-style: none; }
  .contact__item { display: flex; align-items: flex-start; font-size: 22px; line-height: 33px; }
  .contact__icon { width: 26px; height: 33px; margin-right: 12px; flex: none; display: flex; align-items: center; justify-content: center; }
  .contact__icon svg { width: 22px; height: 22px; fill: none; stroke: var(--white); stroke-width: 1.8; }
  .contact__lines { display: flex; flex-direction: column; }
</style>
</head>
<body>
<main class="canvas">

  <section class="card card--front" aria-label="Card front">
    <svg class="card__bands" viewBox="0 0 830 480" aria-hidden="true">
      <defs>
        <linearGradient id="silver-front" x1="0" x2="1" y1="0" y2="0">
          <stop offset="0" stop-color="var(--silver-dark)"/>
          <stop offset="0.5" stop-color="var(--silver-light)"/>
          <stop offset="1" stop-color="var(--silver-dark)"/>
        </linearGradient>
      </defs>
      <path d="M0 350 Q415 305 830 350 L830 480 L0 480 Z" fill="var(--brand-blue)"/>
      <path d="M0 346 Q415 301 830 346" fill="none" stroke="url(#silver-front)" stroke-width="9"/>
    </svg>
    <p class="brand-name">Harbor Lane Freightworks, LLC</p>
    <p class="website">www.harborlanefreightworks.com</p>
  </section>

  <section class="card card--back" aria-label="Card back">
    <svg class="card__bands" viewBox="0 0 830 480" aria-hidden="true">
      <defs>
        <linearGradient id="silver-back" x1="0" x2="1" y1="0" y2="0">
          <stop offset="0" stop-color="var(--silver-dark)"/>
          <stop offset="0.5" stop-color="var(--silver-light)"/>
          <stop offset="1" stop-color="var(--silver-dark)"/>
        </linearGradient>
      </defs>
      <path d="M0 0 H830 V140 Q415 185 0 128 Z" fill="var(--brand-blue)"/>
      <path d="M0 132 Q415 190 830 144" fill="none" stroke="url(#silver-back)" stroke-width="9"/>
    </svg>
    <p class="brand-name">Harbor Lane Freightworks, LLC</p>

    <div class="contact">
      <p class="contact__name">Your Name</p>
      <p class="contact__position">Position</p>
      <ul class="contact__list">
        <li class="contact__item">
          <span class="contact__icon"><svg viewBox="0 0 24 24"><path d="M6 3 L9 3 L10.5 7.5 L8.5 9 Q10 13 15 15.5 L16.5 13.5 L21 15 L21 18 Q20 21 17 21 Q4 19 3 6 Q3 3 6 3 Z"/></svg></span>
          <span>123-456-7890</span>
        </li>
        <li class="contact__item">
          <span class="contact__icon"><svg viewBox="0 0 24 24"><rect x="6" y="2" width="12" height="20" rx="2"/><line x1="10" y1="18.5" x2="14" y2="18.5"/></svg></span>
          <span>123-456-7888</span>
        </li>
        <li class="contact__item">
          <span class="contact__icon"><svg viewBox="0 0 24 24"><rect x="2" y="5" width="20" height="14" rx="1"/><path d="M2 6 L12 13 L22 6"/></svg></span>
          <span>name@companyname.com</span>
        </li>
        <li class="contact__item">
          <span class="contact__icon"><svg viewBox="0 0 24 24"><path d="M12 22 Q5 13 5 9 A7 7 0 0 1 19 9 Q19 13 12 22 Z" fill="var(--white)"/><circle cx="12" cy="9" r="2.5" fill="var(--charcoal)" stroke="none"/></svg></span>
          <span class="contact__lines"><span>Address</span><span>Address</span></span>
        </li>
      </ul>
    </div>
  </section>

</main>
</body>
</html>
```